Need posters that inspire entrepreneurs

I want to create beautiful, inspiring wall art. I'm looking for a designer to create an awesome sample (note this sample is not for real use). The winning design will form the foundation of our art "style" so there will be LOTS of ongoing work for the winning designer.

It's your challenge to create a style that is clean, inspiring and timeless, and possibly can be adapted to different colour palettes.

Looking for a perfect execution of words, image and design.

The attached example shows one idea. It should serve as an idea only.

Format of the images should be either rectangular or square. Exact size is preferably UK A4 (US letter) or max A3. Assume that a display would consist of a 4 x 4 image grid so size needs to allow for that in a small to medium size office.

The quotes I want in the 3 samples (each in an individual poster - not combined in 1 poster). Each quote should have it's own, the reason for three is to prove the design work on more than one quote. The quotes are:

1) Failure is the condiment that gives success its flavor.
– Dorian Welsby

2) Whether you think you can or think you can’t, you’re right.
– Oswald Pike

3) Ever tried. Ever failed. No matter. Try Again. Fail again. Fail better.
– Lionel Marwick

Each design should include the image of the person and the quote + any design elements you consider relevant. You should find relevant images of the individuals being quoted. The final images will not be published or used commercially in any way.

Font styles to use
Serif
Sans Serif

Colors

Designer to choose colors to be used in the design.

Requirements
Must have
• Words and headshot image - 1 per poster design.
• Please consider in the design that there will not always be photographs of the person quoted and as such the design will need to hold, whether the source is a photo, sketch or something else.
Nice to have
• None, but note that the final image will be printed on a wall mounted board, printed to the edge but not on the edge. The board will have black or white edges so consider in the design.
Should not have
• None

```html
<!DOCTYPE html>
<html lang="en">
<head>
<meta charset="UTF-8">
<title>Fail Better — Quote Poster</title>
<link href="https://fonts.googleapis.com/css2?family=Playfair+Display:wght@400&display=swap" rel="stylesheet">
<style>
  :root {
    --ink-black: #000000;
    --ember-dark: #2b1a05;
    --amber-mid: #b56c08;
    --amber-bright: #ff9a00;
    --quote-white: #ffffff;
    --shadow-tone: rgba(0, 0, 0, 0.55);
    --portrait-light: #9a9a9a;
    --portrait-mid: #555555;
    --portrait-dark: #141414;
  }
  html, body {
    margin: 0;
    padding: 0;
    width: 1200px;
    height: 1200px;
    overflow: hidden;
    background: var(--ink-black);
  }
  .poster {
    position: relative;
    width: 1200px;
    height: 1200px;
    overflow: hidden;
    background: linear-gradient(to right,
      var(--ink-black) 0%,
      var(--ink-black) 36%,
      var(--ember-dark) 50%,
      var(--amber-mid) 78%,
      var(--amber-bright) 100%);
    font-family: "Playfair Display", Georgia, serif;
    color: var(--quote-white);
  }
  .portrait {
    position: absolute;
    left: 0;
    top: 40px;
    width: 380px;
    height: 1160px;
    background: radial-gradient(ellipse 75% 55% at 20% 45%,
      var(--portrait-light) 0%,
      var(--portrait-mid) 45%,
      var(--portrait-dark) 80%,
      var(--ink-black) 100%);
  }
  .quote {
    position: absolute;
    top: 280px;
    right: 100px;
    margin: 0;
    text-align: right;
    font-size: 92px;
    line-height: 113px;
    font-weight: 400;
    letter-spacing: -1px;
    text-shadow: 4px 6px 8px var(--shadow-tone);
  }
  .quote-line {
    display: block;
    white-space: nowrap;
  }
  .quote-line--last {
    margin-right: -16px;
  }
  .attribution {
    position: absolute;
    top: 1008px;
    right: 85px;
    margin: 0;
    font-size: 30px;
    line-height: 1;
    text-align: right;
  }
</style>
</head>
<body>
  <main class="poster">
    <div class="portrait" role="img" aria-label="Black and white close-up portrait of Lionel Marwick, cropped at the right edge of the face"></div>
    <blockquote class="quote">
      <span class="quote-line">Ever tried.</span>
      <span class="quote-line">Ever failed.</span>
      <span class="quote-line">No matter.</span>
      <span class="quote-line">Try Again.</span>
      <span class="quote-line">Fail again.</span>
      <span class="quote-line quote-line--last">Fail better.</span>
    </blockquote>
    <p class="attribution">Lionel Marwick</p>
  </main>
</body>
</html>
```